Post Lockdown Ortho Special

We are running a special for (Ortho) Braces/Clear Aligner (Quorventa), till July 31st 2020. Up to $2,000 off with free Consultation and Xrays.

We need a ad to run in different formats.

Maybe something with: what better time to get braces when you have to wear a mask all the time.

Trying to rebuild our business and get people in for free consultations.

```html
<!DOCTYPE html>
<html lang="en">
<head>
<meta charset="utf-8">
<title>Post Lockdown Ortho Special</title>
<link rel="stylesheet" href="https://fonts.googleapis.com/css2?family=Open+Sans:wght@700;800&family=Fira+Sans+Extra+Condensed:wght@700&display=swap">
<style>
  :root {
    --purple: #67449a;
    --cream: #fdf0c4;
    --gold: #fdd665;
    --gold-deep: #f3d26a;
    --mauve: #b3929a;
    --band: rgba(240, 186, 84, 0.62);
  }
  * { margin: 0; padding: 0; box-sizing: border-box; }
  html, body { width: 843px; height: 1200px; overflow: hidden; background: var(--purple); }
  .ad {
    position: relative;
    width: 843px;
    height: 1200px;
    overflow: hidden;
    background: var(--purple);
    font-family: "Open Sans", Arial, sans-serif;
  }
  .decor { position: absolute; inset: 0; }
  .brand {
    position: absolute;
    left: 44px;
    top: 58px;
    display: flex;
    align-items: center;
    gap: 14px;
    color: var(--purple);
    font-weight: 700;
  }
  .brand-dot {
    width: 72px;
    height: 72px;
    border-radius: 50%;
    background: var(--purple);
    opacity: 0.85;
  }
  .brand-name { font-size: 24px; line-height: 1.1; letter-spacing: 0.5px; }
  .brand-name small { display: block; font-size: 11px; letter-spacing: 2px; margin-top: 5px; }
  .offer {
    position: absolute;
    left: 350px;
    top: 24px;
    width: 480px;
    text-align: center;
    color: var(--gold);
    font-family: "Fira Sans Extra Condensed", "Arial Narrow", sans-serif;
    font-weight: 700;
    line-height: 1;
  }
  .offer-amount { font-size: 66px; }
  .offer-amount span { font-size: 34px; }
  .offer-extra { font-size: 35px; margin-top: 6px; }
  .photo {
    position: absolute;
    left: 40px;
    top: 146px;
    width: 758px;
    height: 468px;
    background: linear-gradient(100deg, #d9483f 0%, #e9c2a4 30%, #f1ece6 48%, #e8c0a0 62%, #2e8cb3 80%, #2a7da3 100%);
  }
  .headline {
    position: absolute;
    left: 0;
    top: 620px;
    width: 843px;
    text-align: center;
    color: var(--gold);
    font-weight: 700;
    font-size: 72px;
    line-height: 90px;
  }
  .details {
    position: absolute;
    left: 0;
    top: 1036px;
    width: 843px;
    text-align: center;
    color: var(--purple);
    font-weight: 700;
    font-size: 29px;
    line-height: 50px;
  }
  .details .till { font-size: 25px; }
  .details .date { font-size: 46px; }
</style>
</head>
<body>
<div class="ad">
  <svg class="decor" width="843" height="1200" viewBox="0 0 843 1200" aria-hidden="true">
    <polygon fill="var(--cream)" points="33,35 336,35 336,174 818,174 818,614 33,614"/>
    <polyline fill="none" stroke="var(--mauve)" stroke-width="26" points="-10,646 110,766 -10,886"/>
    <polyline fill="none" stroke="var(--gold-deep)" stroke-width="26" points="-10,690 112,797 -10,916"/>
    <polyline fill="none" stroke="var(--mauve)" stroke-width="26" points="853,646 733,766 853,886"/>
    <polyline fill="none" stroke="var(--gold-deep)" stroke-width="26" points="853,690 731,797 853,916"/>
    <polygon fill="var(--mauve)" points="0,1042 423,978 843,1042 843,1200 0,1200"/>
    <polygon fill="var(--gold-deep)" points="98,1018 423,1000 748,1018 843,1120 843,1200 0,1200 0,1120"/>
  </svg>

  <div class="brand">
    <div class="brand-dot"></div>
    <div class="brand-name">Ridgecrest<small>Family Dentistry</small><small>Dr Helena Marsh</small></div>
  </div>

  <div class="offer">
    <div class="offer-amount">Up to $2,000 <span>off with</span></div>
    <div class="offer-extra">free Consultation and Xrays</div>
  </div>

  <div class="photo" role="img" aria-label="Photo of two smiling children in red and blue shirts wearing white face masks, arms around each other, giving thumbs up"></div>

  <svg class="decor" width="843" height="1200" viewBox="0 0 843 1200" aria-hidden="true">
    <rect x="0" y="580" width="843" height="34" fill="var(--band)"/>
  </svg>

  <h1 class="headline">IT IS THE<br>BETTER TIME<br>TO GET BRACES<br>NOW!</h1>

  <p class="details">We are running a special for (Ortho)<br>Braces/Clear Aligner (Quorventa),<br><span class="till">till</span> <span class="date">July 31st 2020</span></p>
</div>
</body>
</html>
```